Electronic hardware design and manufacturer needing a new business card design.

We need a new business card design consisting of a double sided design adhering to brand and logo guidelines attached. I also want to incorporate something that recognizes our 25th year in business ("EST 2001" or something like that....).

Need extra days to review

Need extra days to review

```html
<!DOCTYPE html>
<html lang="en">
<head>
<meta charset="utf-8">
<title>Northfield Circuit Works – Business Card</title>
<link href="https://fonts.googleapis.com/css2?family=Lato:wght@300;400;700;900&display=swap" rel="stylesheet">
<style>
  :root {
    --stage: #2a2c30;
    --navy: #0b2639;
    --steel: #9bb8d6;
    --white: #ffffff;
    --maroon: #8a2a3c;
    --amber: #f5a81c;
    --orange: #ee6a24;
    --red: #d9352b;
  }
  * { box-sizing: border-box; margin: 0; padding: 0; }
  html, body {
    width: 1200px; height: 952px; overflow: hidden;
    background: var(--stage);
    font-family: "Lato", Arial, sans-serif;
  }
  .sheet {
    width: 1200px; height: 952px;
    display: flex; align-items: center; justify-content: center; gap: 40px;
  }
  .card {
    position: relative;
    width: 540px; height: 309px;
    background: var(--navy);
    border-radius: 4px;
    overflow: hidden;
    box-shadow: 0 14px 30px rgba(0,0,0,.45);
  }

  /* Back face */
  .tab {
    position: absolute;
    width: 150px; height: 46px;
    background: var(--steel);
  }
  .tab--top { top: 0; left: 0; border-radius: 0 0 14px 0; }
  .tab--bottom { bottom: 0; right: 0; border-radius: 14px 0 0 0; }
  .brand {
    position: absolute; display: flex; align-items: center; gap: 12px;
    color: var(--steel); font-weight: 900; letter-spacing: .5px; line-height: 1;
  }
  .brand__mark { background: var(--amber); flex: none; }
  .back .brand { top: 112px; left: 50%; transform: translateX(-50%); }
  .back .brand__name { font-size: 46px; }
  .back .brand__mark { width: 24px; height: 24px; }
  .back .brand__full {
    position: absolute; top: 172px; left: 0; right: 0;
    text-align: center; color: var(--steel);
    font-size: 11px; font-weight: 900; letter-spacing: 2px; text-transform: uppercase;
  }

  /* Front face */
  .front .brand { top: 86px; left: 36px; }
  .front .brand__name { font-size: 42px; }
  .front .brand__mark { width: 20px; height: 20px; }
  .front .brand__full {
    position: absolute; top: 138px; left: 36px;
    color: var(--steel); font-size: 9.5px; font-weight: 900;
    letter-spacing: 1.6px; text-transform: uppercase;
  }
  .person {
    position: absolute; top: 52px; right: 34px; text-align: right;
  }
  .person__name {
    color: var(--steel); font-size: 20px; letter-spacing: 1.6px; text-transform: uppercase;
    font-weight: 300; line-height: 1.1;
  }
  .person__name strong { font-weight: 900; }
  .person__role { color: var(--white); font-size: 13.5px; margin-top: 2px; }
  .person__rule {
    display: block; margin: 10px 0 0 auto; width: 60px; height: 1.5px; background: var(--white);
  }
  .contact {
    position: absolute; right: 34px; bottom: 32px;
    list-style: none; color: var(--white); font-size: 12px; line-height: 1.35;
  }
  .contact__item {
    display: flex; justify-content: flex-end; align-items: center; gap: 8px;
    text-align: right; margin-top: 6px;
  }
  .contact__icon {
    width: 16px; height: 16px; border-radius: 2px; flex: none;
    display: flex; align-items: center; justify-content: center;
  }
  .contact__icon svg { width: 10px; height: 10px; }
  .icon--pin { background: var(--maroon); }
  .icon--phone { background: var(--amber); }
  .icon--mail { background: var(--orange); }
  .icon--web { background: var(--red); }
</style>
</head>
<body>
<main class="sheet">

  <section class="card back" aria-label="Card back">
    <span class="tab tab--top"></span>
    <div class="brand">
      <span class="brand__name">NCW</span>
      <span class="brand__mark"></span>
    </div>
    <p class="brand__full">Northfield Circuit Works</p>
    <span class="tab tab--bottom"></span>
  </section>

  <section class="card front" aria-label="Card front">
    <div class="brand">
      <span class="brand__name">NCW</span>
      <span class="brand__mark"></span>
    </div>
    <p class="brand__full">Northfield Circuit Works</p>

    <div class="person">
      <h1 class="person__name">Daniel R. <strong>Whitmore</strong></h1>
      <p class="person__role">Managing Director</p>
      <span class="person__rule"></span>
    </div>

    <ul class="contact">
      <li class="contact__item">
        <span>1250 Harbor Point Drive<br>Arlington, VA 22201</span>
        <span class="contact__icon icon--pin"><svg viewBox="0 0 10 10"><path d="M5 0.5a3.2 3.2 0 0 0-3.2 3.2C1.8 6.2 5 9.5 5 9.5s3.2-3.3 3.2-5.8A3.2 3.2 0 0 0 5 0.5z" fill="#fff"/><circle cx="5" cy="3.7" r="1.2" fill="#8a2a3c"/></svg></span>
      </li>
      <li class="contact__item">
        <span>+00 555 210 34</span>
        <span class="contact__icon icon--phone"><svg viewBox="0 0 10 10"><path d="M2.2 0.8l1.6 1.8-.9 1.2c.6 1.3 1.6 2.3 2.9 2.9l1.2-.9 1.8 1.6-.9 1.6C4.6 8.8 1.2 5.4 1 1.7z" fill="#fff"/></svg></span>
      </li>
      <li class="contact__item">
        <span>hello@northfieldcircuit.com</span>
        <span class="contact__icon icon--mail"><svg viewBox="0 0 10 10"><rect x="0.8" y="2" width="8.4" height="6" fill="none" stroke="#fff" stroke-width="1"/><path d="M0.8 2L5 5.4 9.2 2" fill="none" stroke="#fff" stroke-width="1"/></svg></span>
      </li>
      <li class="contact__item">
        <span>www.northfieldcircuit.com</span>
        <span class="contact__icon icon--web"><svg viewBox="0 0 10 10"><path d="M5 0.8L8.4 5H6.2v4H3.8V5H1.6z" fill="#fff"/></svg></span>
      </li>
    </ul>
  </section>

</main>
</body>
</html>
```